877 stay Bold

Redesigning this front and back business card flyer and keeping the info but making it look better.

This is all about using the info and logo on the business card design and creating a better layout using any of the following and more.

Changing the background color or imagine, chaining the placement of content, resizing content.

Target Market(s)

Targeting people that have been injured on one side and people that have been giving a DUI on the other.

Contact Information for Business Card

We are looking to keep the info but make it look a fee cleaner and less cluttered

Font styles to use
Sans Serif

Requirements
Must have
• Must have the same info but a better layout.
Nice to have
• better background colors or image or layout. different fonts or same font all design options that will make it look professional and clean.

```html
<!DOCTYPE html>
<html lang="en">
<head>
<meta charset="utf-8">
<title>877 stay Bold – Business Card Front and Back</title>
<link rel="stylesheet" href="https://fonts.googleapis.com/css2?family=Titan+One&family=Didact+Gothic&display=swap">
<style>
  :root {
    --page: #e6e6e6;
    --card: #ffffff;
    --ink: #1c1c1c;
    --band: #231f20;
    --red: #d0121b;
    --muted: #f2f2f2;
    --photo-night: #3a2a3a;
    --photo-floor: #a9a6a0;
    --photo-room: #2b3036;
  }
  * { box-sizing: border-box; margin: 0; padding: 0; }
  html, body { width: 1200px; height: 900px; overflow: hidden; }
  body {
    background: var(--page);
    font-family: "Didact Gothic", "Century Gothic", sans-serif;
    color: var(--ink);
    position: relative;
  }
  .card {
    position: absolute;
    width: 720px;
    height: 411px;
    background: var(--card);
    border-radius: 18px;
    overflow: hidden;
    box-shadow: 0 6px 18px rgba(0,0,0,0.18);
  }
  .card--dui { left: 240px; top: 30px; }
  .card--injury { left: 240px; top: 459px; }

  .brand-band {
    position: absolute;
    top: 0; bottom: 0;
    width: 170px;
    background: var(--band);
    display: flex;
    align-items: center;
    justify-content: center;
  }
  .card--dui .brand-band { left: 0; border-right: 5px solid var(--red); }
  .card--injury .brand-band { right: 0; border-left: 5px solid var(--red); }

  .brand-name {
    writing-mode: vertical-rl;
    font-family: "Titan One", "Gill Sans", sans-serif;
    font-size: 44px;
    line-height: 1;
    color: #ffffff;
    white-space: nowrap;
    display: flex;
    align-items: center;
    gap: 14px;
  }
  .card--dui .brand-name { transform: rotate(180deg); }
  .brand-mark {
    width: 22px; height: 22px;
    background: var(--red);
    display: inline-block;
  }

  .card-body {
    position: absolute;
    top: 26px;
  }
  .card--dui .card-body { left: 200px; right: 24px; }
  .card--injury .card-body { left: 30px; right: 200px; }

  .call {
    font-family: "Titan One", "Gill Sans", sans-serif;
    color: var(--red);
    font-size: 34px;
    line-height: 1.05;
    letter-spacing: 0.5px;
  }
  .web {
    font-family: "Titan One", "Gill Sans", sans-serif;
    color: var(--ink);
    font-size: 22px;
    line-height: 1.2;
    margin-top: 2px;
  }
  .headline {
    font-family: "Titan One", "Gill Sans", sans-serif;
    color: var(--red);
    font-size: 30px;
    line-height: 1.1;
    margin-top: 8px;
  }
  .subhead {
    font-family: "Titan One", "Gill Sans", sans-serif;
    color: var(--ink);
    font-size: 13.5px;
    margin-top: 4px;
    padding-bottom: 6px;
    border-bottom: 1.5px solid var(--red);
  }
  .tip-list {
    list-style: none;
    margin-top: 8px;
    font-size: 17px;
    line-height: 1.42;
  }
  .tip-list li {
    display: flex;
    align-items: baseline;
    gap: 8px;
  }
  .tip-list .note { font-size: 11px; color: var(--ink); }
  .no-icon {
    width: 12px; height: 12px;
    flex: none;
    position: relative;
    top: 1px;
  }
  .continuation { padding-left: 20px; }

  .card--injury .headline { font-size: 27px; margin-top: 10px; white-space: nowrap; }
  .card--injury .tip-list { font-size: 18px; line-height: 1.32; margin-top: 6px; }

  .photo-row {
    display: flex;
    gap: 14px;
    margin-top: 14px;
  }
  .photo {
    width: 150px;
    height: 78px;
  }
  .photo--crash { background: linear-gradient(135deg, var(--photo-night), #7a4050); }
  .photo--crutch { background: linear-gradient(135deg, var(--photo-floor), #d8d4cc); }
  .photo--recovery { background: linear-gradient(135deg, var(--photo-room), #7d8790); }

  .tagline {
    font-family: "Titan One", "Gill Sans", sans-serif;
    color: var(--red);
    font-size: 16.5px;
    margin-top: 14px;
    white-space: nowrap;
  }
</style>
</head>
<body>

<svg width="0" height="0" style="position:absolute" aria-hidden="true">
  <symbol id="no-sign" viewBox="0 0 12 12">
    <circle cx="6" cy="6" r="4.6" fill="none" stroke="#d0121b" stroke-width="2"/>
    <line x1="2.8" y1="9.2" x2="9.2" y2="2.8" stroke="#d0121b" stroke-width="2"/>
  </symbol>
</svg>

<section class="card card--dui">
  <div class="brand-band">
    <div class="brand-name"><span class="brand-mark"></span>877 stay Bold</div>
  </div>
  <div class="card-body">
    <p class="call">CALL 877-555-0142</p>
    <p class="web">www.877staybold.com</p>
    <h2 class="headline">STAY BOLD FOR A DUI</h2>
    <p class="subhead">WHAT SHOULD I DO IF I GET PULLED OVER FOR DUI?</p>
    <ul class="tip-list">
      <li><svg class="no-icon"><use href="#no-sign"/></svg>Pull over in a calm, normal manner</li>
      <li><svg class="no-icon"><use href="#no-sign"/></svg>Be polite at all times</li>
      <li><svg class="no-icon"><use href="#no-sign"/></svg>Do not admit to drinking</li>
      <li><svg class="no-icon"><use href="#no-sign"/></svg>Do not submit to any field sobriety tests</li>
      <li><svg class="no-icon"><use href="#no-sign"/></svg><span>Do not submit to taking a chemical test <span class="note">(breath, blood, or urine)</span></span></li>
      <li><svg class="no-icon"><use href="#no-sign"/></svg>Do not make any statement after being arrested,</li>
      <li class="continuation">especially when placed in the police cruiser</li>
    </ul>
  </div>
</section>

<section class="card card--injury">
  <div class="brand-band">
    <div class="brand-name"><span class="brand-mark"></span>877 stay Bold</div>
  </div>
  <div class="card-body">
    <p class="call">CALL 877-555-0142</p>
    <p class="web">www.877staybold.com</p>
    <h2 class="headline">If You've Been Injured STAY BOLD</h2>
    <ul class="tip-list">
      <li><svg class="no-icon"><use href="#no-sign"/></svg>for an inexperienced lawyer!</li>
      <li><svg class="no-icon"><use href="#no-sign"/></svg>for less than you deserve!</li>
      <li><svg class="no-icon"><use href="#no-sign"/></svg>for paying massive medical bills!</li>
      <li><svg class="no-icon"><use href="#no-sign"/></svg>for a life of pain and debt!</li>
    </ul>
    <div class="photo-row">
      <div class="photo photo--crash" role="img" aria-label="Photo of a damaged car at a night-time accident scene with emergency lights"></div>
      <div class="photo photo--crutch" role="img" aria-label="Photo of a leg in a walking boot beside a crutch"></div>
      <div class="photo photo--recovery" role="img" aria-label="Photo of a person in a wheelchair silhouetted by a window"></div>
    </div>
    <p class="tagline">We fight for you, so you can focus on getting better</p>
  </div>
</section>

</body>
</html>
```